Web design for a pet services marketplace

I represent a South American based company: “TORVELIS” which provides a different array of pet related services. As a starting point, I would like to get proposals for 1 page website (plus a general frame for forms, instructions etc) web design job for a dog boarding marketplace. If you could add a logo is desirable.
By a Dog Boarding Marketplace, I mean a community marketplace, very much like an roomswap, but for pet services (initially dog boarding/daycare, but evolving to other services such as dog walkers. The purpose is to bring together dog owners and dog-care providers according to qualifications or characteristics given at time of input and needs of the dog owner given at the time of searching. Providers create a profile, entering certain information requested in forms such as their location, type of house/apt, what type/size of dogs they take, prior experience, as well as a personal introduction and pictures. Providers will set their own rates and calendar availability. Then customers browse, schedule and book and pay online. As it works for similar services, there will be a system of reviews and feedback for each care provider.
As to the website, it should be substantially similar to the following websites: (www.pupstayo.com , www.kelbo.com). It should be simple and straightforward, prioritizing ease of use. I would like for visitors to easily understand how the model works by seeing the home page, and getting pop up explanations by browsing over each main icon or message on the homepage. Therefore, I would try to keep additional pages to a minimum.
As I’m new to this, I would not venture as to how many pages I would need and would defer to your suggestion, according to the examples provided. However, I would like to have a visually striking front end, with dog related pictures or cartoon type images. Icons etc should be fun, and related to dogs, vacations, hotels/lodging, travel, etc. Secondary pages (like enrollment forms, Q&A, etc) could have a clean design, maybe adding some non-obtrusive related imagery.
Please note that attached pictures are , third party property and are for guide only.
Additional info:
In general I want to make a site very much like the examples of pupstayo and kelbo, but i think a better job could be done in terms of design. Please feel free to provide your own ideas.
1. For now, since the site will be new, we would not be including a testimonials section. However, we could use the space , or maybe smaller, with the "spread the love"section for announcing special deals for people who share the project.
2. In the principal section, I would like to see a clean layout. Much like pupstayo does. As an alternative, I would also like to see how it would look like if we handled more cartoon type drawings instead of pictures (just a suggestion to see how it would look like).
3. Search spaces should be more floating (merging more with background), as in pupstayo, not in larger boxes.
Updates
Please find in the attachments a very rough wire frame that i just did as response to a project proposal. Please note where i say OK (top and bottom) I mean that those two sections i found ok in such project or the model websites. Pretty regular content in those sections. Added Friday, July 10, 2015
Target Market(s)
dog owners, people who are willing to host pets in their home, kennels
Industry/Entity Type
Pet Care
Number of Pages Required
1 page
Look and feel

```html
<!DOCTYPE html>
<html lang="en">
<head>
<meta charset="UTF-8">
<title>TORVELIS – Trusted Dog Sitters</title>
<link rel="stylesheet" href="https://fonts.googleapis.com/css2?family=Open+Sans:wght@300;400;600;700&family=Roboto+Condensed:wght@400;700&display=swap">
<style>
:root{
  --ink:#333a40;
  --muted:#8a9096;
  --orange:#e2522a;
  --sky-top:#b7d3e6;
  --sky-bottom:#dfe9ee;
  --steel:#5f7f98;
  --step-bg:#ececec;
  --step-num:#c9c9c9;
  --rose:#c49597;
  --rose-dark:#b4878a;
  --photo-dark:#4f2e1d;
  --photo-light:#c48d5e;
  --footer-bar:#9db1c2;
  --white:#ffffff;
}
*{box-sizing:border-box;margin:0;padding:0}
html,body{width:747px;height:1200px;overflow:hidden}
body{font-family:"Open Sans",Arial,sans-serif;color:var(--ink);background:var(--white);position:relative}

/* Header */
.site-header{position:absolute;left:0;top:0;width:747px;height:90px;background:var(--white)}
.brand{position:absolute;left:60px;top:16px;display:flex;align-items:center;gap:10px}
.brand-mark{width:42px;height:42px;border-radius:50%;background:var(--steel)}
.brand-name{font-family:"Roboto Condensed",sans-serif;font-weight:700;font-size:30px;color:var(--ink);line-height:1}
.brand-tag{font-size:13px;color:var(--steel);margin-top:3px}
.account{position:absolute;left:425px;top:18px;text-align:center;font-size:10px;color:var(--muted)}
.account a{color:var(--muted);text-decoration:none}
.btn-host{display:block;margin-top:6px;background:var(--orange);color:var(--white);font-size:10px;font-weight:600;padding:5px 10px;border-radius:2px}
.support{position:absolute;right:58px;top:16px;text-align:right}
.support-label{font-size:11px;color:var(--muted)}
.support-phone{font-size:24px;color:var(--ink);font-weight:400;line-height:1.2}

/* Hero */
.hero{position:absolute;left:0;top:90px;width:747px;height:322px}
.hero-art{position:absolute;inset:0;background:linear-gradient(180deg,var(--sky-top) 0%,#c9dde9 55%,var(--sky-bottom) 100%)}
.hero-title{position:absolute;left:78px;top:76px;font-family:"Roboto Condensed",sans-serif;font-weight:700;font-size:22px;color:var(--white);letter-spacing:.5px}
.search{position:absolute;left:78px;top:110px;width:330px}
.search-row{display:flex;gap:6px;margin-bottom:8px;align-items:center}
.field{background:var(--white);border:1px solid #c5cdd3;height:26px;font-size:11px;color:var(--ink);padding:5px 8px}
.field-city{width:216px}
.btn-find{background:var(--steel);color:var(--white);font-size:11px;font-weight:600;height:26px;padding:6px 10px;border:1px solid var(--white)}
.option{display:flex;align-items:center;gap:4px;background:var(--white);height:24px;padding:0 7px;font-size:10px}
.radio{width:9px;height:9px;border:1px solid #8a9096;border-radius:50%}
.field-date{width:64px;height:24px;padding:4px 6px;font-size:10px}
.hero-arrow{position:absolute;top:140px;width:26px;height:34px;background:rgba(255,255,255,.85);display:flex;align-items:center;justify-content:center}
.hero-arrow.prev{left:30px}
.hero-arrow.next{right:30px}
.help-tab{position:absolute;right:0;top:365px;width:18px;height:72px;background:var(--orange);color:var(--white);font-size:8px;font-weight:700;writing-mode:vertical-rl;display:flex;align-items:center;justify-content:center;letter-spacing:1px}

/* Steps */
.steps{position:absolute;left:0;top:412px;width:747px;height:260px;background:var(--step-bg)}
.step{position:absolute;top:42px;width:230px;height:150px}
.step-num{position:absolute;left:0;top:-18px;font-family:"Roboto Condensed",sans-serif;font-size:170px;line-height:1;color:var(--step-num);font-weight:400}
.step-card{position:absolute;left:46px;top:18px;width:170px;height:112px;background:var(--white);padding:14px 12px 0 14px}
.step-icon{position:absolute;right:22px;top:12px}
.step-title{font-family:"Roboto Condensed",sans-serif;font-size:24px;color:#6f757a;margin-top:30px;letter-spacing:1px}
.step-text{font-size:9px;color:var(--muted);margin-top:2px;line-height:1.3}
.step-more{position:absolute;right:6px;bottom:6px;width:12px;height:12px;background:#ccc}

/* Trust */
.trust{position:absolute;left:0;top:672px;width:747px;height:175px;background:var(--rose)}
.trust-item{position:absolute;top:28px;width:230px;text-align:center;color:var(--white)}
.trust-icon{display:block;margin:0 auto 8px}
.trust-title{font-family:"Roboto Condensed",sans-serif;font-weight:700;font-size:29px;line-height:1.1}
.trust-text{font-size:9px;opacity:.9;margin-top:3px}

/* Share */
.share{position:absolute;left:0;top:847px;width:747px;height:162px}
.share-art{position:absolute;inset:0;background:linear-gradient(90deg,var(--photo-dark) 0%,#7a4b2e 45%,var(--photo-light) 75%,#8c5a37 100%)}
.share-copy{position:absolute;left:52px;top:28px;width:270px;color:var(--white)}
.share-title{font-size:32px;font-weight:300;line-height:1.1}
.share-text{font-size:12px;margin-top:8px;line-height:1.4}
.btn-share{display:inline-block;margin-top:12px;background:var(--orange);color:var(--white);font-size:12px;font-weight:600;padding:8px 16px;letter-spacing:.5px}

/* Footer */
.site-footer{position:absolute;left:0;top:1009px;width:747px;height:166px;background:var(--white)}
.foot-col{position:absolute;top:36px;font-size:8.5px;color:var(--ink);line-height:1.6}
.foot-col h4{font-size:8.5px;font-weight:700;margin-bottom:6px;letter-spacing:.3px}
.foot-col ul{list-style:none}
.news-text{font-size:8px;color:var(--muted);margin-bottom:8px}
.news-form{display:flex}
.news-input{width:112px;height:20px;border:1px solid #c5cdd3;font-size:8px;color:var(--muted);padding:4px 6px}
.news-btn{height:20px;background:var(--steel);color:var(--white);font-size:8px;padding:4px 8px}
.social{display:flex;gap:7px;margin-top:6px}
.social span{width:22px;height:22px;border-radius:50%;background:var(--steel)}
.foot-bar{position:absolute;left:0;top:1175px;width:747px;height:25px;background:var(--footer-bar);color:var(--white);font-size:8px;text-align:center;line-height:25px}
</style>
</head>
<body>

<header class="site-header">
  <div class="brand">
    <span class="brand-mark"></span>
    <div>
      <div class="brand-name">TORVELIS</div>
      <div class="brand-tag">Trusted Dog Sitters</div>
    </div>
  </div>
  <div class="account">
    <a href="#">Login</a> | <a href="#">Signup</a>
    <span class="btn-host">Become a Sitter</span>
  </div>
  <div class="support">
    <div class="support-label">Customer Support</div>
    <div class="support-phone">800-555-0193</div>
  </div>
</header>

<section class="hero">
  <div class="hero-art" role="img" aria-label="Cartoon scene of dogs with a suitcase beside a hotel, a globe and a plane in a pale blue sky"></div>
  <h1 class="hero-title">FIND A LOVING DOG SITTER</h1>
  <form class="search">
    <div class="search-row">
      <span class="field field-city">City</span>
      <span class="btn-find">FIND SITTER</span>
    </div>
    <div class="search-row">
      <span class="option"><span class="radio"></span>Over Night</span>
      <span class="option"><span class="radio"></span>Day Care</span>
      <span class="field field-date">Start</span>
      <span class="field field-date">End</span>
    </div>
  </form>
  <span class="hero-arrow prev"><svg width="10" height="14" viewBox="0 0 10 14"><path d="M8 1 2 7l6 6" fill="none" stroke="#5f7f98" stroke-width="2"/></svg></span>
  <span class="hero-arrow next"><svg width="10" height="14" viewBox="0 0 10 14"><path d="M2 1l6 6-6 6" fill="none" stroke="#5f7f98" stroke-width="2"/></svg></span>
</section>

<div class="help-tab">HELP</div>

<section class="steps">
  <div class="step" style="left:34px">
    <span class="step-num">1</span>
    <div class="step-card">
      <svg class="step-icon" width="26" height="26" viewBox="0 0 26 26"><circle cx="11" cy="11" r="7" fill="none" stroke="#e2522a" stroke-width="2.5"/><path d="M16 16l7 7" stroke="#e2522a" stroke-width="3"/></svg>
      <div class="step-title">SEARCH</div>
      <p class="step-text">Browse loving, trusted dog sitters near you.</p>
      <span class="step-more"></span>
    </div>
  </div>
  <div class="step" style="left:268px">
    <span class="step-num">2</span>
    <div class="step-card">
      <svg class="step-icon" width="26" height="26" viewBox="0 0 26 26"><rect x="3" y="5" width="20" height="18" fill="none" stroke="#e2522a" stroke-width="2.5"/><path d="M3 10h20M8 2v5M18 2v5" stroke="#e2522a" stroke-width="2.5"/></svg>
      <div class="step-title">BOOK</div>
      <p class="step-text">Get to know your sitter at a Meet &amp; Greet.</p>
      <span class="step-more"></span>
    </div>
  </div>
  <div class="step" style="left:500px">
    <span class="step-num">3</span>
    <div class="step-card">
      <svg class="step-icon" width="26" height="26" viewBox="0 0 26 26"><rect x="3" y="8" width="20" height="15" rx="2" fill="none" stroke="#e2522a" stroke-width="2.5"/><path d="M9 8V4h8v4" fill="none" stroke="#e2522a" stroke-width="2.5"/></svg>
      <div class="step-title">RELAX</div>
      <p class="step-text">You'll enjoy text and photo updates.</p>
      <span class="step-more"></span>
    </div>
  </div>
</section>

<section class="trust">
  <div class="trust-item" style="left:20px">
    <svg class="trust-icon" width="54" height="54" viewBox="0 0 54 54"><path d="M27 4 46 11v15c0 12-8 20-19 24C16 46 8 38 8 26V11Z" fill="#fff"/><path d="M19 27l6 6 11-12" fill="none" stroke="#c49597" stroke-width="4"/></svg>
    <div class="trust-title">Insured Pets</div>
    <p class="trust-text">Reservations include 24/7 customer support</p>
  </div>
  <div class="trust-item" style="left:258px">
    <svg class="trust-icon" width="54" height="54" viewBox="0 0 54 54"><circle cx="27" cy="27" r="26" fill="#fff"/><ellipse cx="27" cy="33" rx="9" ry="7" fill="#c49597"/><circle cx="17" cy="22" r="4" fill="#c49597"/><circle cx="24" cy="16" r="4" fill="#c49597"/><circle cx="31" cy="16" r="4" fill="#c49597"/><circle cx="38" cy="22" r="4" fill="#c49597"/></svg>
    <div class="trust-title">Velted Hosts</div>
    <p class="trust-text">Screened and trusted by us</p>
  </div>
  <div class="trust-item" style="left:497px">
    <svg class="trust-icon" width="54" height="54" viewBox="0 0 54 54"><path d="M5 27 27 7l22 20h-6v20H11V27Z" fill="#fff"/><path d="M27 40c-6-4-9-7-9-11a4 4 0 0 1 9-1 4 4 0 0 1 9 1c0 4-3 7-9 11Z" fill="#c49597"/></svg>
    <div class="trust-title">One On One TLC</div>
    <p class="trust-text">Your pup stays in their home or yours</p>
  </div>
</section>

<section class="share">
  <div class="share-art" role="img" aria-label="Photo of a smiling girl hugging a long-eared spaniel"></div>
  <div class="share-copy">
    <h2 class="share-title">Spread the Love</h2>
    <p class="share-text">Tell a friend about TORVELIS, and they'll get $10 off their first reservation.</p>
    <span class="btn-share">START SHARING</span>
  </div>
</section>

<footer class="site-footer">
  <div class="foot-col" style="left:58px">
    <h4>HELP</h4>
    <ul><li>Support Center</li><li>How it Works</li><li>Contact Us</li><li>Concierge</li></ul>
  </div>
  <div class="foot-col" style="left:178px">
    <h4>YOU MAY NEED THIS</h4>
    <ul><li>Home</li><li>Contact us</li><li>FAQ</li><li>Terms &amp; conditions</li><li>Privacy policy</li></ul>
  </div>
  <div class="foot-col" style="left:318px">
    <h4>HOSTING</h4>
    <ul><li>Become a Sitter</li><li>How Hosting Works</li><li>Hosting Tips</li><li>Hosting Policy</li></ul>
  </div>
  <div class="foot-col" style="left:488px">
    <h4>NEWS &amp; DEALS BY EMAIL</h4>
    <p class="news-text">Hear first about our latest news and exclusive deals</p>
    <div class="news-form"><span class="news-input">Email Address</span><span class="news-btn">Subscribe</span></div>
    <h4 style="margin-top:10px;margin-bottom:0">STAY CONNECTED ON</h4>
    <div class="social"><span></span><span></span><span></span></div>
  </div>
</footer>
<div class="foot-bar">© 2015 TORVELIS . All Rights Reserved</div>

</body>
</html>
```